Quillbrook Medical Business Card Design

This is a private medical device company. We recently launched the new website and would like to redesign the business cards. Please see the website: www.quillbrookmedical.example. We'd like to keep the cards simple and professional but modern to match the website and collateral branding. Our customers are physicians and investors. I have attached the old design for comparison. I have also attached the updated logo. Please note the business card information will change, based on all employees who need to order them. So I will need to be able easily edit the copy.
Updates

Hi designers-thank you very much for submitting designs. I look forward to the results!! Joan

Target Market(s)

Our target audience are physicians

Industry/Entity Type

Medical

Contact Information for Business Card

Dorothy Wensley
Director of Marketing and Reimbursement
dwensley@quillbrookmedical.example
M: xxx-xxx-xxxx
O: xxx-xxx-xxxx
4120 Pinto Ridge Rd.
Suite 610
Austin, TX 78592

Font styles to use
Sans Serif

Requirements
Must have
• Must include the logo and a color or color from the logo and branding
Nice to have
• Maybe include the logo icon on the back.

```html
<!DOCTYPE html>
<html lang="en">
<head>
<meta charset="utf-8">
<title>Quillbrook Medical Business Card</title>
<link href="https://fonts.googleapis.com/css2?family=Open+Sans:wght@400;600&family=Questrial&display=swap" rel="stylesheet">
<style>
  :root {
    --stage-dark: #0b0b0b;
    --stage-light: #2e2e2e;
    --card: #ffffff;
    --teal: #74b9cc;
    --teal-deep: #5a9fb0;
    --red: #ee3a4c;
    --ink: #3c3838;
    --ink-soft: #4a4a4a;
    --faint: #f3f1f1;
  }
  * { margin: 0; padding: 0; box-sizing: border-box; }
  html, body { width: 1200px; height: 1000px; overflow: hidden; }
  body {
    position: relative;
    background: radial-gradient(ellipse at 50% 48%, var(--stage-light) 0%, #1a1a1a 45%, var(--stage-dark) 100%);
    font-family: "Open Sans", sans-serif;
  }
  .card {
    position: absolute;
    left: 275px;
    width: 629px;
    height: 368px;
    background: var(--card);
    overflow: hidden;
  }
  .card--front { top: 97px; }
  .card--back { top: 512px; height: 369px; }

  /* Front */
  .front-brand {
    position: absolute;
    left: 0; right: 0; top: 160px;
    display: flex; justify-content: center; align-items: center; gap: 16px;
  }
  .front-brand__dot {
    width: 22px; height: 22px; border-radius: 50%; background: var(--red);
  }
  .front-brand__name {
    font-size: 38px; font-weight: 600; color: var(--ink); letter-spacing: 0.5px;
  }
  .front-url {
    position: absolute; left: 0; right: 0; top: 292px;
    text-align: center;
    font-family: "Questrial", sans-serif;
    font-size: 14px; letter-spacing: 3px; color: #222;
  }

  /* Back */
  .accent-bar {
    position: absolute; left: 0; top: 0; bottom: 0; width: 12px; background: var(--teal);
  }
  .faint-circle {
    position: absolute; left: 330px; top: 130px;
    width: 330px; height: 330px; border-radius: 50%;
    background: var(--faint);
  }
  .brand {
    position: absolute; left: 44px; top: 56px;
    display: flex; align-items: center; gap: 10px;
  }
  .brand__square { width: 36px; height: 36px; background: var(--teal-deep); }
  .brand__name { font-size: 25px; font-weight: 400; color: var(--ink); }
  .person {
    position: absolute; right: 58px; top: 58px; text-align: right;
  }
  .person__name { font-size: 19px; font-weight: 600; color: #1e1e1e; line-height: 1.2; }
  .person__title { font-size: 10.5px; color: #333; margin-top: 8px; }
  .contact {
    position: absolute; left: 45px; top: 217px; list-style: none;
    font-size: 14px; color: var(--ink-soft);
  }
  .contact__row { display: flex; align-items: center; height: 27px; white-space: nowrap; }
  .contact__icon {
    width: 17px; height: 17px; background: var(--teal);
    display: flex; align-items: center; justify-content: center;
    margin-right: 13px; flex: none;
  }
  .contact__icon svg { width: 11px; height: 11px; }
  .contact__row--plain { padding-left: 30px; }
  .contact__gap { margin-left: 16px; }
</style>
</head>
<body>

<section class="card card--front">
  <div class="front-brand">
    <span class="front-brand__dot"></span>
    <span class="front-brand__name">Quillbrook Medical</span>
  </div>
  <p class="front-url">www.quillbrookmedical.example</p>
</section>

<section class="card card--back">
  <div class="accent-bar"></div>
  <div class="faint-circle"></div>

  <div class="brand">
    <span class="brand__square"></span>
    <span class="brand__name">Quillbrook Medical</span>
  </div>

  <div class="person">
    <p class="person__name">Dorothy Wensley</p>
    <p class="person__title">Director of Marketing and Reimbursement</p>
  </div>

  <ul class="contact">
    <li class="contact__row">
      <span class="contact__icon">
        <svg viewBox="0 0 12 12" fill="none" stroke="#fff" stroke-width="1.1">
          <circle cx="6" cy="6" r="5"/><ellipse cx="6" cy="6" rx="2.2" ry="5"/><line x1="1" y1="6" x2="11" y2="6"/>
        </svg>
      </span>
      dwensley@quillbrookmedical.example
    </li>
    <li class="contact__row">
      <span class="contact__icon">
        <svg viewBox="0 0 12 12" fill="#fff">
          <path d="M2.5 1 L4.5 1 L5.2 3.6 L4 4.6 C4.6 6 5.8 7.3 7.3 8 L8.3 6.8 L11 7.5 L11 9.5 C11 10.3 10.3 11 9.5 11 C5 11 1 7 1 2.5 C1 1.7 1.7 1 2.5 1 Z"/>
        </svg>
      </span>
      M: xxx-xxx-xxxx<span class="contact__gap">O: xxx-xxx-xxxx</span>
    </li>
    <li class="contact__row">
      <span class="contact__icon">
        <svg viewBox="0 0 12 12" fill="#fff">
          <path d="M6 1 L11.5 6 L10 6 L10 11 L7.3 11 L7.3 8 L4.7 8 L4.7 11 L2 11 L2 6 L0.5 6 Z"/>
        </svg>
      </span>
      4120 Pinto Ridge Rd. Suite 610
    </li>
    <li class="contact__row contact__row--plain">Austin, TX 78592</li>
  </ul>
</section>

</body>
</html>
```